The Honeycrisp Are Ready: Announcing Apple Picking At Dorn & Wexley

I would like to develop an e-mail notification to send to our subscribers notifying them:
(Announcing to our fans that Honeycrisp Apples are ready for picking)

Header: The Honeycrisp Are Ready!
Now Picking Our Family Favorite Variety
We Wanted To Make Sure You Were The First To Know

Cedar Knoll Is Open 7 Days A Week For Apple Picking

These Will Not Last Long!

Fall Is Back At Dorn & Wexley. This Means Cool, Crisp Fall Days In The Orchard. Warm Cider Donuts & Apple Fritters, Hard Cider Sampling, Pony Rides, Apple Picking & Much More. Come Join Us And Make Fall Memories That Will Last For Generations To Come.

Target Market(s)

Families Looking For Activities In The Fall

Industry/Entity Type

Agri-Tourism

Font styles to use
Other font styles liked:
• DDC Hardware

Colors
0054AA
0677BA
7BADD7
CADEEF
E8F1F8
EB3D1F
EC4F4E
F09395
F8D3D4
FCEDEE

Requirements
Must have
• Call To Action: The Honeycrisp Are Ready!
Nice to have
• Images of the orchard and people picking apples. Please take a look at our website: www.dornandwexley.example for inspiration

```html
<!DOCTYPE html>
<html lang="en">
<head>
<meta charset="utf-8">
<title>The Honeycrisp Are Ready! – Dorn &amp; Wexley</title>
<link rel="stylesheet" href="https://fonts.googleapis.com/css2?family=Bebas+Neue&family=Kaushan+Script&family=Caveat+Brush&display=swap">
<style>
  :root {
    --paper: #ebe7e2;
    --photo-light: #e4dfd9;
    --photo-dark: #cfc9c2;
    --ink: #111111;
    --apple-red: #d7222a;
    --sketch: #bdb5ad;
  }
  html, body {
    margin: 0;
    padding: 0;
    overflow: hidden;
    background: var(--paper);
  }
  .email-card {
    position: relative;
    width: 1200px;
    height: 867px;
    overflow: hidden;
    background: var(--paper);
    font-family: "Bebas Neue", "Arial Narrow", sans-serif;
    color: var(--ink);
  }
  .farm-backdrop {
    position: absolute;
    inset: 0;
    background: linear-gradient(180deg, var(--paper) 0%, var(--photo-light) 35%, var(--photo-dark) 62%, var(--photo-light) 100%);
    opacity: .9;
  }
  .art {
    position: absolute;
    border-radius: 6px;
  }
  .art--sign { left: 281px; top: 174px; width: 85px; height: 192px; background: linear-gradient(180deg, #d6d0c9, #c4bdb5); }
  .art--basket { left: 85px; top: 388px; width: 218px; height: 192px; background: radial-gradient(circle at 55% 55%, #bfb6ad, #d3ccc4 75%); }
  .art--tree { left: 816px; top: 116px; width: 344px; height: 455px; background: radial-gradient(ellipse at 50% 30%, #c5bdb4, #d8d2cb 70%); }
  .art--truck { left: 763px; top: 656px; width: 365px; height: 156px; background: linear-gradient(180deg, #3a3636, #161414); }
  .art--apples { left: 682px; top: 767px; width: 76px; height: 49px; background: #d4cec7; border-radius: 24px; }

  .headline {
    position: absolute;
    left: 272px;
    top: 42px;
    margin: 0;
    font-size: 100px;
    line-height: 1;
    font-weight: 400;
    letter-spacing: -1px;
  }
  .headline-script {
    position: absolute;
    left: 420px;
    top: 140px;
    margin: 0;
    font-family: "Kaushan Script", cursive;
    font-size: 66px;
    font-weight: 400;
    color: var(--apple-red);
    line-height: 1.2;
  }
  .rule {
    position: absolute;
    height: 3px;
    background: var(--ink);
    border-radius: 2px;
  }
  .rule--top { left: 433px; top: 241px; width: 214px; }
  .rule--bottom { left: 491px; top: 570px; width: 223px; }

  .variety {
    position: absolute;
    right: 460px;
    top: 280px;
    margin: 0;
    text-align: right;
    font-size: 50px;
    line-height: 58px;
    font-weight: 400;
  }
  .first-line {
    position: absolute;
    left: 281px;
    top: 422px;
    margin: 0;
    font-size: 50px;
    line-height: 1;
    white-space: nowrap;
  }
  .first-line .chevron { font-size: 32px; vertical-align: 6px; margin-right: 10px; }
  .first-know {
    position: absolute;
    left: 446px;
    top: 484px;
    margin: 0;
    font-size: 72px;
    line-height: 1;
    color: var(--apple-red);
    white-space: nowrap;
  }
  .hours {
    position: absolute;
    left: 219px;
    top: 603px;
    margin: 0;
    font-size: 37px;
    letter-spacing: 4.6px;
    line-height: 1;
    white-space: nowrap;
  }
  .dots {
    position: absolute;
    left: 428px;
    top: 666px;
  }
  .last-call {
    position: absolute;
    left: 205px;
    top: 690px;
    margin: 0;
    font-family: "Caveat Brush", cursive;
    font-size: 54px;
    line-height: 1.1;
    font-weight: 400;
    white-space: nowrap;
  }
</style>
</head>
<body>
<main class="email-card">
  <div class="farm-backdrop" role="img" aria-label="Faded photo of the Dorn &amp; Wexley farm market with barn, entrance sign and picnic tables"></div>

  <div class="art art--sign" role="img" aria-label="Sketch of a wooden Cedar Knoll signpost"></div>
  <div class="art art--basket" role="img" aria-label="Sketch of a woven basket full of apples"></div>
  <div class="art art--tree" role="img" aria-label="Sketch of an apple tree with red apples and a ladder"></div>
  <div class="art art--truck" role="img" aria-label="Silhouette of a vintage pickup truck loaded with apples"></div>
  <div class="art art--apples" role="img" aria-label="Sketch of two apples on the ground"></div>

  <h1 class="headline">The Honeycrisp</h1>
  <p class="headline-script">Are Ready!</p>
  <div class="rule rule--top"></div>

  <p class="variety">Now picking our family<br>favorite variety</p>

  <p class="first-line"><span class="chevron">›</span>We wanted to make sure you were the</p>
  <p class="first-know">First to know</p>
  <div class="rule rule--bottom"></div>

  <p class="hours">Cedar Knoll is open 7 days a week for apple picking</p>
  <svg class="dots" width="42" height="10" viewBox="0 0 42 10" aria-hidden="true">
    <circle cx="5" cy="5" r="3.5" fill="#111"/>
    <circle cx="21" cy="5" r="3.5" fill="#111"/>
    <circle cx="37" cy="5" r="3.5" fill="#111"/>
  </svg>
  <p class="last-call">These Will Not Last Long!</p>
</main>
</body>
</html>
```